Candle company needs a label for candle

Looking for a designer to create my candle label. I am going to attach a few pictures of my vision for the label as well as my Company Logo and jar I have puchased. I'm going for the modern rustic feel but you are the designer and have full trust in your abilities. The label is going to be printed on Kraft paper (2x3) so looking for the font to be black. The candle label MUST include the following information:
Candle Birchway Co.
NO. 01: Eucalyptus + Spearmint
Handmade In NJ
Soy Wax
9oz

Industry/Entity Type

Candle Industry

Colors

Designer to choose colors to be used in the design.

Requirements
Should not have
• Any images

```html
<!DOCTYPE html>
<html lang="en">
<head>
<meta charset="UTF-8">
<title>Candle Birchway Co. — No. 01 Label</title>
<link href="https://fonts.googleapis.com/css2?family=Righteous&family=Old+Standard+TT:wght@400&display=swap" rel="stylesheet">
<style>
  :root {
    --canvas: #2b2b2b;
    --paper-light: #faf6ec;
    --paper-mid: #f1e8d3;
    --paper-edge: #d9c7a3;
    --ink: #141414;
    --rule: #8a8170;
  }
  * { margin: 0; padding: 0; box-sizing: border-box; }
  html, body {
    width: 720px; height: 1200px; overflow: hidden;
    background: var(--canvas);
  }
  .canvas { position: relative; width: 720px; height: 1200px; }
  .label {
    position: absolute; left: 40px; top: 385px;
    width: 640px; height: 430px;
    background: radial-gradient(ellipse at 50% 45%, var(--paper-light) 0%, var(--paper-mid) 60%, var(--paper-edge) 100%);
    color: var(--ink);
  }
  .brand {
    position: absolute; left: 80px; top: 52px;
    display: flex; align-items: center; gap: 10px;
    font-family: "Old Standard TT", Georgia, serif;
    font-size: 22px; line-height: 1; color: var(--ink);
  }
  .brand-mark {
    width: 12px; height: 12px; background: var(--ink);
  }
  .scent-number {
    position: absolute; left: 78px; top: 138px;
    font-family: "Righteous", "Arial Black", sans-serif;
    font-weight: 400; font-size: 96px; line-height: 1; letter-spacing: 2px;
    color: var(--ink);
  }
  .scent-name {
    position: absolute; left: 80px; top: 232px;
    width: 480px; height: 44px;
    border: 1.5px solid var(--rule);
    display: flex; align-items: center; justify-content: center;
    font-family: "Righteous", "Arial Black", sans-serif;
    font-size: 28px; letter-spacing: 1.5px; color: var(--ink);
  }
  .origin {
    position: absolute; left: 80px; top: 296px;
    font-family: "Old Standard TT", Georgia, serif;
    font-size: 34px; line-height: 1.2; color: var(--ink);
  }
  .specs {
    position: absolute; left: 80px; top: 348px;
    display: flex; height: 46px;
    border: 1.5px solid var(--rule);
    font-family: "Old Standard TT", Georgia, serif;
    font-size: 30px; color: var(--ink);
  }
  .spec { display: flex; align-items: center; padding: 0 16px; }
  .spec + .spec { border-left: 1.5px solid var(--rule); }
</style>
</head>
<body>
  <main class="canvas">
    <section class="label">
      <div class="brand"><span class="brand-mark"></span><span class="brand-name">Candle Birchway Co.</span></div>
      <h1 class="scent-number">NO. 01:</h1>
      <p class="scent-name">Eucalyptus + Spearmint</p>
      <p class="origin">Handmade In NJ</p>
      <div class="specs">
        <span class="spec">Soy Wax</span>
        <span class="spec">9oz</span>
      </div>
    </section>
  </main>
</body>
</html>
```